Business Card design for insurance broker in Denver, CO, USA

I need a business card designed using this logo that was just created. We sell life and disability income insurance to US consumers.
Looking for a professionally designed card to make use of the logo and have something to hand to prospects or new business referral sources. The card could be white, gray, black or whatever you would recommend.

Target Market(s)

US Consumers and other financial professionals that I partner with.

Industry/Entity Type

Insurance Broker

Contact Information for Business Card

Owen R. Tessler, CLU, LUTCF (please note that CLU should have a superscript R in a circle for registered trademark)
President
phone (303) 555-0147
email owen@brightlakecoverage.com
4620 W. Hollister Rd, Suite 310, Alder Springs, CO 80999
Somewhere fit in a tagline saying "Your resource for life, long term care, and disability insurance" (maybe the back if it doesn't fit on the front, your call)

Font styles to use
Sans Serif

Requirements
Must have
• Must have logo in correct blue and gray colors, my name, address, phone, email. Order and placement determined by the designer.
• I just want something that looks a more professional than what I could have done using the business card designer tool on printmakerhub.com or CardNest, or any other do-it-yourself tool
• A regular rectangular business card with square corners is preferred
Nice to have
• I included the logos of 2 organizations I belong to (GQLF and BEPWO). They should be small, but visible on the back only. If it doesn’t look good, this is not a requirement, feel free to drop it.
Should not have
• Do not add any colors not already in the logo, except use of black and whites which are okay. If you use the logo on the back and want to make that in all black, gray or white, that may be okay as well.

```html
<!DOCTYPE html>
<html lang="en">
<head>
<meta charset="utf-8">
<title>Brightlake Coverage – Business Cards</title>
<link href="https://fonts.googleapis.com/css2?family=Roboto:wght@400;500;700&display=swap" rel="stylesheet">
<style>
  :root {
    --stage: #dfe0e2;
    --ink: #231f20;
    --paper: #ffffff;
    --brand-blue: #2a8ad2;
    --badge-soft: #5f7ea8;
    --rule: #8c8c8c;
  }
  html, body {
    margin: 0;
    padding: 0;
    width: 1200px;
    height: 768px;
    overflow: hidden;
    background: var(--stage);
    font-family: "Roboto", Arial, sans-serif;
  }
  p { margin: 0; }
  .canvas { position: relative; width: 1200px; height: 768px; }
  .card {
    position: absolute;
    width: 502px;
    height: 286px;
    box-shadow: 0 2px 8px rgba(0,0,0,0.12);
    overflow: hidden;
  }
  .card--back    { left: 349px; top: 78px;  background: var(--ink); }
  .card--front-a { left: 78px;  top: 404px; background: var(--paper); }
  .card--front-b { left: 620px; top: 399px; background: var(--paper); }

  /* brand lockup: plain ring + name */
  .brand { position: absolute; display: flex; align-items: center; gap: 18px; }
  .brand__ring {
    width: 74px; height: 74px; border-radius: 50%;
    border: 4px solid var(--brand-blue); box-sizing: border-box;
  }
  .brand__name {
    color: var(--brand-blue);
    font-weight: 500;
    font-size: 25px;
    line-height: 23px;
    letter-spacing: 0.5px;
  }

  .card--back .brand { left: 105px; top: 95px; }
  .tagline {
    position: absolute; left: 0; right: 0; top: 252px;
    text-align: center; color: var(--paper);
    font-size: 12.5px; font-weight: 500; line-height: 16px;
  }

  /* front A */
  .side-band { position: absolute; left: 0; top: 0; width: 58px; height: 100%; background: var(--ink); }
  .ring-plate {
    position: absolute; width: 82px; height: 82px; border-radius: 50%;
    background: var(--paper); display: flex; align-items: center; justify-content: center;
  }
  .ring-plate .brand__ring { width: 72px; height: 72px; }
  .card--front-a .ring-plate { left: 15px; top: 20px; }
  .card--front-a .brand__name { position: absolute; left: 109px; top: 37px; }
  .badges { position: absolute; left: 360px; top: 36px; display: flex; gap: 18px; }
  .badge--round { width: 44px; height: 44px; border-radius: 50%; background: var(--badge-soft); }
  .badge--tri { width: 0; height: 0;
    border-left: 24px solid transparent; border-right: 24px solid transparent;
    border-bottom: 36px solid var(--brand-blue); margin-top: 4px; }

  .person__name { font-size: 16px; font-weight: 700; color: var(--ink); line-height: 20px; }
  .person__name sup { font-size: 9px; }
  .person__title { font-size: 12.5px; color: var(--brand-blue); margin-top: 3px; }
  .contact { list-style: none; margin: 0; padding: 0; font-size: 12.5px; color: var(--ink); }
  .contact li { display: flex; align-items: center; gap: 6px; height: 18px; }
  .contact svg { width: 11px; height: 11px; fill: var(--brand-blue); flex: none; }

  .card--front-a .person { position: absolute; left: 100px; top: 167px; }
  .card--front-a .contact { position: absolute; left: 98px; top: 215px; }

  /* front B */
  .top-tab { position: absolute; left: 29px; top: 0; width: 72px; height: 32px; background: var(--ink); }
  .card--front-b .ring-plate { left: 25px; top: 25px; }
  .card--front-b .brand__name { position: absolute; left: 115px; top: 44px; }
  .card--front-b .person { position: absolute; right: 29px; top: 173px; text-align: right; }
  .divider { position: absolute; left: 29px; right: 29px; top: 221px; height: 1px; background: var(--rule); }
  .card--front-b .contact { position: absolute; left: 29px; top: 233px; }
  .address { position: absolute; right: 29px; top: 233px; text-align: right;
    font-size: 12.5px; line-height: 18px; color: var(--ink); font-style: normal; }
</style>
</head>
<body>
<div class="canvas">

  <section class="card card--back">
    <div class="brand">
      <div class="brand__ring"></div>
      <div class="brand__name">BRIGHTLAKE<br>COVERAGE</div>
    </div>
    <p class="tagline">Your resource for life, long term care, and disability insurance</p>
  </section>

  <section class="card card--front-a">
    <div class="side-band"></div>
    <div class="ring-plate"><div class="brand__ring"></div></div>
    <div class="brand__name">BRIGHTLAKE<br>COVERAGE</div>
    <div class="badges">
      <div class="badge--round" role="img" aria-label="GQLF membership badge"></div>
      <div class="badge--tri" role="img" aria-label="BEPWO membership badge"></div>
    </div>
    <div class="person">
      <p class="person__name">Owen R. Tessler, CLU<sup>®</sup>, LUTCF</p>
      <p class="person__title">President</p>
    </div>
    <ul class="contact">
      <li><svg viewBox="0 0 24 24"><path d="M6.6 10.8a15.1 15.1 0 0 0 6.6 6.6l2.2-2.2c.3-.3.7-.4 1-.2 1.1.4 2.3.6 3.6.6.6 0 1 .4 1 1V20c0 .6-.4 1-1 1A17 17 0 0 1 3 4c0-.6.4-1 1-1h3.5c.6 0 1 .4 1 1 0 1.3.2 2.5.6 3.6.1.3 0 .7-.2 1z"/></svg>(303) 555-0147</li>
      <li><svg viewBox="0 0 24 24"><path d="M2 5h20v14H2z M2 5l10 8 10-8"/></svg>owen@brightlakecoverage.com</li>
      <li><svg viewBox="0 0 24 24"><path d="M12 2a7 7 0 0 0-7 7c0 5 7 13 7 13s7-8 7-13a7 7 0 0 0-7-7zm0 9.5A2.5 2.5 0 1 1 12 6.5a2.5 2.5 0 0 1 0 5z"/></svg>4620 W. Hollister Rd, Suite 310, Alder Springs, CO 80999</li>
    </ul>
  </section>

  <section class="card card--front-b">
    <div class="top-tab"></div>
    <div class="ring-plate"><div class="brand__ring"></div></div>
    <div class="brand__name">BRIGHTLAKE<br>COVERAGE</div>
    <div class="person">
      <p class="person__name">Owen R. Tessler, CLU<sup>®</sup>, LUTCF</p>
      <p class="person__title">President</p>
    </div>
    <div class="divider"></div>
    <ul class="contact">
      <li><svg viewBox="0 0 24 24"><path d="M6.6 10.8a15.1 15.1 0 0 0 6.6 6.6l2.2-2.2c.3-.3.7-.4 1-.2 1.1.4 2.3.6 3.6.6.6 0 1 .4 1 1V20c0 .6-.4 1-1 1A17 17 0 0 1 3 4c0-.6.4-1 1-1h3.5c.6 0 1 .4 1 1 0 1.3.2 2.5.6 3.6.1.3 0 .7-.2 1z"/></svg>(303) 555-0147</li>
      <li><svg viewBox="0 0 24 24"><path d="M2 5h20v14H2z M2 5l10 8 10-8"/></svg>owen@brightlakecoverage.com</li>
    </ul>
    <address class="address">4620 W. Hollister Rd, Suite 310<br>Alder Springs, CO 80999</address>
  </section>

</div>
</body>
</html>
```